Corvella Web Design Project

I am attaching my logo so I need to see applied to the website developed by you guys!!
Tbahks!!
Ferruccio
This is the DNA of the company
Flat and dynamic organization - Informal and respectful social approac
Innovative - Always striving for the best solution
Reliability and Quality - The value of our name
Flexibility - Ability to handle new requirements and unforeseen events
Simplicity - Technology must serve – NOT rule!
Cooperative Relations - The synergy that makes 1+1=3
We still don´t have our logo as we have another open project on artbazaarly
Our company won´t be selling this equipment but providing welding services for shipyard industry, as you can see on the website below.
www.velmorasystems.example
Reason: Hi webdesigners,
I will be deciding my logo by this weekend as soon as I have decided I will post my logo to see it applied to your design!!!
Thanks
Ferruccio
I just Sent my logo for your attention!!!!
Welding

```html
<!DOCTYPE html>
<html lang="en">
<head>
<meta charset="utf-8">
<title>Corvella – Robotic Welding Technologie</title>
<link href="https://fonts.googleapis.com/css2?family=Lato:wght@400;700&display=swap" rel="stylesheet">
<style>
:root{
  --olive:#978f33;
  --olive-dark:#7d7628;
  --ink:#2b2b2b;
  --text:#3a3a3a;
  --muted:#6b6b6b;
  --btn:#3f3f3f;
  --line:#d6d6d6;
  --white:#ffffff;
}
*{box-sizing:border-box;margin:0;padding:0}
html,body{width:1106px;height:1200px;overflow:hidden}
body{font-family:'Lato',sans-serif;color:var(--text);
  background:radial-gradient(ellipse at 50% 55%,#e4e4e4 0%,#f3f3f3 45%,#fafafa 75%,#ffffff 100%)}
.canvas{position:relative;width:1106px;height:1200px}
.frame{position:absolute;left:167px;top:12px;width:771px;height:1105px;border:1px solid #bdbdbd;background:#f4f4f4}
.page{position:absolute;left:7px;top:7px;width:755px;height:1089px;background:var(--white);border:1px solid #d2d2d2}
/* all children below positioned relative to .page (origin 175,19) */
.abs{position:absolute}
.logo{left:14px;top:17px;display:flex;align-items:center;gap:6px}
.logo-mark{width:48px;height:48px;border-radius:50%;background:var(--olive)}
.logo-name{font-size:46px;font-weight:400;color:#444;line-height:1;letter-spacing:-.5px}
.logo-tag{left:67px;top:64px;font-size:8px;letter-spacing:.6px;color:#444}
.nav{right:24px;top:42px;display:flex;gap:21px;font-size:12px;color:#444}
.nav .active{color:var(--olive);font-weight:700}

.hero{left:15px;top:96px;width:726px;height:197px;
  background:linear-gradient(100deg,#22305a 0%,#2c3f7a 30%,#6a4a2a 55%,#c9732a 72%,#f3c27a 85%,#e9a04a 100%)}
.hero-shadow{left:40px;top:293px;width:680px;height:20px;
  background:radial-gradient(ellipse at 50% 0%,rgba(0,0,0,.28),rgba(0,0,0,0) 70%)}
.caption{left:32px;top:46px;width:264px;height:104px;background:rgba(235,235,240,.9);border-radius:3px;padding:12px 10px}
.caption h2{font-size:17px;font-weight:400;color:var(--olive);margin-bottom:6px}
.caption p{font-size:7.6px;line-height:14px;color:var(--ink)}
.caption .btn-olive{display:inline-block;margin-top:5px;background:var(--olive);color:#fff;font-size:8px;font-weight:700;padding:4px 6px;border:2px solid #fff;box-shadow:0 0 0 1px #ccc}
.arrow{width:20px;height:20px;border-radius:50%;background:var(--olive);border:2px solid #fff;top:197px;display:flex;align-items:center;justify-content:center}
.arrow svg{width:8px;height:8px}
.dots{left:490px;top:282px;display:flex;gap:5px}
.dots span{width:10px;height:10px;border-radius:50%;background:#fff}
.dots span.on{background:var(--olive);border:2px solid #fff}

.intro h3{font-size:17.5px;font-weight:400;color:var(--ink);margin-bottom:14px}
.intro p{font-size:8.4px;line-height:13.2px;color:var(--ink)}
.intro p+p{margin-top:13px}

.card{width:230px}
.card .shot{width:230px;height:102px;border:2px solid #fff;box-shadow:0 0 3px rgba(0,0,0,.35)}
.card h4{font-size:13px;font-weight:400;color:var(--ink);margin-top:13px}
.card h4 em{font-style:normal;color:var(--olive)}
.card p{font-size:8.6px;line-height:10.5px;color:var(--muted);margin-top:18px;height:48px}
.card .learn{display:inline-block;margin-top:9px;background:var(--btn);color:#fff;font-size:8px;font-weight:700;padding:3px 6px;box-shadow:1px 1px 2px rgba(0,0,0,.4)}

.more-tab{left:746px;top:671px;width:21px;height:108px;background:var(--olive);border-radius:0 14px 14px 0;display:flex;align-items:center;justify-content:center}
.more-tab span{writing-mode:vertical-rl;font-size:7.5px;font-weight:700;color:#fff;letter-spacing:.3px}

.band{left:14px;top:990px;width:727px;height:85px;background:var(--olive);overflow:hidden}
.band h5{position:absolute;left:11px;top:9px;font-size:17.5px;font-weight:400;color:#111}
.band h5 b{color:#fff}
.band .q{position:absolute;left:11px;top:37px;font-size:7.6px;font-weight:700;color:#111}
.band .find{position:absolute;left:11px;top:49px;font-size:7.6px;color:#222}
.band .calc-btn{position:absolute;left:11px;top:60px;background:var(--btn);color:#fff;font-size:8px;font-weight:700;padding:4px 6px}
.band .calc{position:absolute;left:388px;top:8px}
.band .divider{position:absolute;left:495px;top:8px;width:1px;height:70px;background:#d8d4a8}
.band .follow{position:absolute;left:520px;top:9px;font-size:17px;font-weight:700;color:#fff}
.band .social{position:absolute;left:515px;top:33px;display:flex;gap:6px}
.band .social span{width:40px;height:40px;border-radius:50%;background:#fff}

.foot-nav{left:0;top:1130px;width:1106px;display:flex;justify-content:center;gap:13px;font-family:Arial,sans-serif;font-size:9.5px;color:#111}
.foot-nav i{font-style:normal}
.foot-copy{left:0;top:1148px;width:1106px;text-align:center;font-family:Arial,sans-serif;font-size:7.6px;color:#111}
</style>
</head>
<body>
<div class="canvas">
  <div class="frame">
    <div class="page">
      <div class="abs logo"><span class="logo-mark"></span><span class="logo-name">Corvella</span></div>
      <div class="abs logo-tag">ROBOTIC WELDING TECHNOLOGIE</div>
      <nav class="abs nav"><span class="active">Home</span><span>About us</span><span>Competence</span><span>Case Story</span><span>Products</span><span>Videos</span></nav>

      <div class="abs hero" role="img" aria-label="Photo of a robotic welder throwing bright orange sparks over a steel plate"></div>
      <div class="abs hero-shadow"></div>
      <div class="abs caption" style="left:47px;top:142px">
        <h2>Corvella</h2>
        <p>Lorem Ipsum is simply dummy text of the printing and typesetting industry. Lorem Ipsum has been the industry's standard</p>
        <span class="btn-olive">READ MORE</span>
      </div>
      <div class="abs arrow" style="left:5px"><svg viewBox="0 0 8 8"><path d="M5.5 1 2.5 4l3 3" stroke="#fff" stroke-width="1.6" fill="none"/></svg></div>
      <div class="abs arrow" style="left:731px"><svg viewBox="0 0 8 8"><path d="M2.5 1l3 3-3 3" stroke="#fff" stroke-width="1.6" fill="none"/></svg></div>
      <div class="abs dots"><span class="on"></span><span></span><span></span></div>

      <section class="abs intro" style="left:17px;top:326px;width:354px">
        <h3>Welcome to Corvella.</h3>
        <p>Lorem Ipsum is simply dummy text of the printing and typesetting industry. Lorem Ipsum has been the industry's standard dummy text ever since the 1500s, when an unknown printer took a galley of type and scrambled it to make a type specimen book. It has survived not only five centuries, but also the leap into electronic typesetting, remaining essentially unchanged. It was popularised in the 1960s with the release of Lettrafix sheets containing Lorem Ipsum passages, and more recently with desktop publishing software like Pagewright Studio including versions of Lorem Ipsum.</p>
      </section>
      <section class="abs intro" style="left:388px;top:326px;width:352px">
        <h3>About us</h3>
        <p>Lorem Ipsum is simply dummy text of the printing and typesetting industry. Lorem Ipsum has been the industry's standard dummy text ever since the 1500s, when an unknown printer took a galley of type and scrambled it to make a type specimen book.</p>
        <p>It has survived not only five centuries, but also the leap into electronic typesetting, remaining essentially unchanged. It was popularised in the 1960s with the release of Lettrafix sheets containing Lorem Ipsum passages, and more recently with desktop publishing software like Pagewright Studio including versions of Lorem Ipsum.</p>
      </section>

      <article class="abs card" style="left:15px;top:485px">
        <div class="shot" role="img" aria-label="Orange welding robot arm on an olive overlay with a zoom icon" style="background:#a39b4a"></div>
        <h4>General <em>Features</em></h4>
        <p>Lorem Ipsum has been the industry's standard dummy text ever since the 1500s, when an unknown printer took a galley of type and scrambled it to make a type specimen book</p>
        <span class="learn">LEARN MORE</span>
      </article>
      <article class="abs card" style="left:263px;top:485px">
        <div class="shot" role="img" aria-label="Rendering of a yellow mini crawler welding robot on a rail" style="background:linear-gradient(135deg,#d9d9d9,#c9c9b0 55%,#e6dfa2)"></div>
        <h4>Mini Crawler <em>Welding Robot</em></h4>
        <p>Lorem Ipsum has been the industry's standard dummy text ever since the 1500s, when an unknown printer took a galley of type and scrambled it to make a type specimen book</p>
        <span class="learn">LEARN MORE</span>
      </article>
      <article class="abs card" style="left:511px;top:485px">
        <div class="shot" role="img" aria-label="Photo of a gantry welding robot inside a workshop" style="background:linear-gradient(160deg,#8d8a86,#3c4a66 55%,#2a3550)"></div>
        <h4>Gantry Welding <em>Robot</em></h4>
        <p>Lorem Ipsum has been the industry's standard dummy text ever since the 1500s, when an unknown printer took a galley of type and scrambled it to make a type specimen book</p>
        <span class="learn">LEARN MORE</span>
      </article>

      <article class="abs card" style="left:15px;top:736px">
        <div class="shot" role="img" aria-label="Rendering of a high rail welding robot on a platform with green railings" style="background:linear-gradient(160deg,#d8ddd6,#b9b7a4 60%,#8f7e5a)"></div>
        <h4>Hight Rail <em>Welding Robot</em></h4>
        <p>Lorem Ipsum has been the industry's standard dummy text ever since the 1500s, when an unknown printer took a galley of type and scrambled it to make a type specimen book</p>
        <span class="learn">LEARN MORE</span>
      </article>
      <article class="abs card" style="left:263px;top:736px">
        <div class="shot" role="img" aria-label="Photo of orange industrial robot arms on a welding platform" style="background:linear-gradient(135deg,#c8702c,#6f6a66 50%,#3b3f4a)"></div>
        <h4>Platform&nbsp; <em>Welding Robot</em></h4>
        <p>Lorem Ipsum has been the industry's standard dummy text ever since the 1500s, when an unknown printer took a galley of type and scrambled it to make a type specimen book</p>
        <span class="learn">LEARN MORE</span>
      </article>
      <article class="abs card" style="left:511px;top:736px">
        <div class="shot" role="img" aria-label="Rendering of a micro panel welding robot inside a steel panel grid" style="background:linear-gradient(135deg,#8d8d95,#a8a8b2 55%,#b9bc6a)"></div>
        <h4>Micro Panel <em>Welding Robot</em></h4>
        <p>Lorem Ipsum has been the industry's standard dummy text ever since the 1500s, when an unknown printer took a galley of type and scrambled it to make a type specimen book</p>
        <span class="learn">LEARN MORE</span>
      </article>

      <div class="abs more-tab"><span>MORE PRODUCTS</span></div>

      <section class="abs band">
        <h5>Online <b>Free Estimate Calculator</b></h5>
        <div class="q">No sure of budget? Or Price Range of options?</div>
        <div class="find">Find out immediately how much the Corvella you want will cost...<b>more</b></div>
        <span class="calc-btn">Free Estimate Calculator</span>
        <svg class="calc" width="80" height="84" viewBox="0 0 80 84" aria-hidden="true">
          <g transform="rotate(14 40 42)">
            <rect x="14" y="6" width="52" height="84" rx="8" fill="#fff"/>
            <rect x="21" y="14" width="38" height="14" rx="2" fill="#978f33"/>
            <g fill="#978f33">
              <circle cx="27" cy="40" r="4"/><circle cx="40" cy="40" r="4"/><circle cx="53" cy="40" r="4"/>
              <circle cx="27" cy="53" r="4"/><circle cx="40" cy="53" r="4"/><circle cx="53" cy="53" r="4"/>
              <circle cx="27" cy="66" r="4"/><circle cx="40" cy="66" r="4"/><circle cx="53" cy="66" r="4"/>
            </g>
          </g>
        </svg>
        <span class="divider"></span>
        <div class="follow">Follow us on</div>
        <div class="social" aria-label="Social links"><span></span><span></span><span></span></div>
      </section>
    </div>
  </div>

  <nav class="abs foot-nav"><span>HOME</span><i>I</i><span>ABOUT US</span><i>I</i><span>COMPETENCE</span><i>I</i><span>CASE STORY</span><i>I</i><span>PRODUCTS</span><i>I</i><span>VIDEOS</span></nav>
  <div class="abs foot-copy">© 2014 Corvella. All rights reserved.</div>
</div>
</body>
</html>
```